Zielgruppe
Die travlon GmbH bietet professionelle Cloud-Lösungen im Bereich spezialisierter Verwaltungssysteme. Hierbei handelt es sich um Software as a Service (SaaS), die zu 100% von der travlon GmbH betrieben und kontinuierlich weiterentwickelt wird.
Aufgabenstellung
Das Design kann Farben und/oder Elemente der travlon GmbH enthalten (www.travlon.de). Da es sich um ein eigenen Produkt handelt, muss jedoch auch Neutralität bewahrt werden.

```html
<!DOCTYPE html>
<html lang="de">
<head>
<meta charset="utf-8">
<title>Domora – Domain registrieren</title>
<link href="https://fonts.googleapis.com/css2?family=Roboto:wght@400;500;700&display=swap" rel="stylesheet">
<style>
  :root{
    --red:#e31e24;
    --blue:#3c5d8c;
    --white:#ffffff;
    --ink:#1c1c1c;
    --muted:#8a8a8a;
    --line:#dcdcdc;
    --band:#9e9e9e;
    --soft:#f4f4f4;
    --green:#1fbf7a;
  }
  *{box-sizing:border-box;margin:0;padding:0}
  html,body{width:1200px;height:1193px;overflow:hidden;background:var(--white)}
  body{font-family:"Roboto",Arial,sans-serif;color:var(--ink)}
  .page{position:absolute;left:0;top:0;width:1920px;height:1909px;transform:scale(.625);transform-origin:0 0}

  .topbar{position:absolute;left:0;top:0;width:1920px;height:100px;background:var(--red);color:var(--white)}
  .brand{position:absolute;left:279px;top:34px;display:flex;align-items:center;gap:10px;font-size:27px;font-weight:500}
  .brand-dot{width:32px;height:32px;border-radius:50%;border:2.5px solid var(--white)}
  .notice{position:absolute;left:976px;display:flex;align-items:center;gap:9px;font-size:14px}
  .meta{position:absolute;top:24px;font-size:14px}
  .user{position:absolute;left:1505px;top:24px;font-size:14px;font-weight:700}
  .session{position:absolute;left:1505px;top:49px;width:135px;height:7px;background:var(--white);border-radius:3px;overflow:hidden}
  .session span{display:block;width:96px;height:100%;background:var(--green)}
  .session-label{position:absolute;left:1505px;top:65px;font-size:12px}
  .logout{position:absolute;left:1803px;top:43px;display:flex;align-items:center;gap:8px;font-size:14px;font-weight:500}

  .mainnav{position:absolute;left:0;top:100px;width:1920px;height:56px;background:var(--white)}
  .mainnav a{position:absolute;top:20px;font-size:14px;font-weight:500;color:var(--ink);text-decoration:none}
  .mainnav a.active{color:var(--red)}
  .mainnav a.active::after{content:"";position:absolute;left:0;right:0;top:33px;height:3px;background:var(--red)}

  .stage{position:absolute;left:0;top:156px;width:1920px;height:1644px;background:var(--blue)}

  .sidebar{position:absolute;left:280px;top:204px;width:316px;height:812px;background:var(--white);border-radius:3px}
  .sidebar .item{position:absolute;left:16px;width:284px;height:41px;padding-left:16px;display:flex;align-items:center;font-size:16px;font-weight:400;border-radius:4px}
  .sidebar .item.active{background:var(--red);color:var(--white);font-weight:500}
  .sidebar .item svg{position:absolute;right:0}

  .card{position:absolute;left:628px;width:1012px;background:var(--white);border-radius:4px;overflow:hidden}
  .card::before{content:"";position:absolute;left:0;top:0;right:0;height:10px;background:var(--band)}
  .card.primary::before{background:var(--red)}
  .card-title{position:absolute;left:32px;top:34px;font-size:20px;font-weight:500}
  .label{position:absolute;font-size:14px;font-weight:500;transform:translateY(-50%)}
  .field{position:absolute;height:32px;border:1px solid var(--line);border-radius:4px;background:var(--white);font-size:14px;display:flex;align-items:center;padding:0 12px}
  .field.focus{border:2px solid #f3a7aa;box-shadow:0 0 0 1px #fbe0e1}
  .select{color:var(--muted);justify-content:space-between}
  .btn{position:absolute;height:35px;border-radius:4px;background:var(--red);color:var(--white);font-size:14px;font-weight:700;display:flex;align-items:center;justify-content:center}
  .btn.ghost{background:var(--white);color:var(--red);border:1px solid var(--red);font-weight:500}
  .more{position:absolute;right:32px;top:35px;display:flex;align-items:center;gap:8px;font-size:14px;font-weight:500}
  .plus{width:22px;height:22px;border:1px solid #eee;border-radius:3px;display:flex;align-items:center;justify-content:center;color:var(--muted);font-size:16px}

  .intro{position:absolute;left:32px;top:79px;width:800px;font-size:14px;line-height:22px}
  .contact{position:absolute;left:32px;width:948px;height:111px;border:1px solid #e4e4e4;border-radius:3px}
  .contact-head{height:47px;background:var(--soft);border-bottom:1px solid #e4e4e4;display:flex;align-items:center;padding:0 16px;font-size:14px;font-weight:500}
  .mode{margin-left:auto;display:flex;align-items:center;gap:8px;font-weight:400}
  .mode b{font-weight:500;margin-right:8px}
  .check{width:16px;height:16px;border:1px solid #bbb;border-radius:3px;display:inline-flex;align-items:center;justify-content:center}
  .check.on{background:var(--green);border-color:var(--green)}
  .mode .gap{margin-right:8px}
  .contact-row{position:relative;height:63px}
  .contact-row .name{position:absolute;left:15px;top:32px;transform:translateY(-50%);font-size:14px}
  .contact-row .field{left:282px;top:16px;width:242px}
  .icon-btn{position:absolute;top:17px;width:30px;height:30px;border:1px solid var(--line);border-radius:4px;display:flex;align-items:center;justify-content:center}

  .footer-btn{position:absolute;left:1448px;top:1833px;width:192px;height:45px;border-radius:4px;background:var(--red);color:var(--white);font-size:16px;font-weight:700;display:flex;align-items:center;justify-content:center}
</style>
</head>
<body>
<div class="page">

  <header class="topbar">
    <div class="brand"><span class="brand-dot"></span>Domora</div>
    <div class="notice" style="top:24px">
      <svg width="16" height="12" viewBox="0 0 16 12"><rect x="0" y="0" width="16" height="12" rx="1" fill="#fff"/><path d="M1 1l7 6 7-6" stroke="#e31e24" stroke-width="1.5" fill="none"/></svg>
      neue Nachrichten
    </div>
    <div class="notice" style="top:48px">
      <svg width="16" height="16" viewBox="0 0 16 16"><circle cx="8" cy="8" r="8" fill="#fff"/><path d="M8 4v4.5l3 1.5" stroke="#e31e24" stroke-width="1.6" fill="none"/></svg>
      Aufragsstapel
    </div>
    <div class="meta" style="left:1305px">Version: 2.2.8</div>
    <div class="meta" style="left:1406px">Sitemap</div>
    <div class="user">angemeldet als jola</div>
    <div class="session"><span></span></div>
    <div class="session-label">120 min. Restzeit</div>
    <div class="logout">
      <svg width="17" height="15" viewBox="0 0 17 15" fill="none" stroke="#fff" stroke-width="1.6"><path d="M8 1H1v13h7"/><path d="M5 7.5h11M13 4.5l3 3-3 3"/></svg>
      Logout
    </div>
  </header>

  <nav class="mainnav">
    <a style="left:280px">Start</a>
    <a style="left:359px">Benutzer</a>
    <a style="left:463px">Kontakt</a>
    <a class="active" style="left:560px">Domain</a>
    <a style="left:656px">DNS</a>
  </nav>

  <div class="stage"></div>

  <aside class="sidebar">
    <div class="item" style="top:17px">Domain Liste</div>
    <div class="item active" style="top:65px">Domain registrieren</div>
    <div class="item" style="top:115px">Domain transferieren</div>
    <div class="item" style="top:164px">Domain bearbeiten</div>
    <div class="item" style="top:213px">Domain wiederherstellen</div>
    <div class="item" style="top:262px">Messenaufrage</div>
    <div class="item" style="top:311px">DNSSEC<svg width="12" height="8" viewBox="0 0 12 8"><path d="M1 1l5 5 5-5" stroke="#333" stroke-width="1.8" fill="none"/></svg></div>
    <div class="item" style="top:360px">Werkzeug<svg width="12" height="8" viewBox="0 0 12 8"><path d="M1 1l5 5 5-5" stroke="#333" stroke-width="1.8" fill="none"/></svg></div>
  </aside>

  <section class="card primary" style="top:204px;height:154px">
    <h2 class="card-title">Domain</h2>
    <span class="label" style="left:32px;top:106px">Domain*</span>
    <div class="field focus" style="left:178px;top:88px;width:244px;height:35px">domora.co<span style="display:inline-block;width:1px;height:16px;background:#000"></span></div>
    <div class="btn" style="left:876px;top:88px;width:104px">Welter</div>
  </section>

  <section class="card" style="top:391px;height:206px">
    <h2 class="card-title">Domain-Vorlage</h2>
    <div class="more">Wreiter optionen <span class="plus">+</span></div>
    <span class="label" style="left:32px;top:106px">Domain-Vorlage*</span>
    <div class="field" style="left:180px;top:89px;width:240px"></div>
    <div class="btn" style="left:780px;top:88px;width:200px">Vorlage laden</div>
    <span class="label" style="left:32px;top:157px">Voreinsstellung*</span>
    <div class="field select" style="left:180px;top:141px;width:240px">Bitte wahlen
      <svg width="11" height="7" viewBox="0 0 11 7"><path d="M1 1l4.5 4.5L10 1" stroke="#444" stroke-width="1.5" fill="none"/></svg></div>
    <div class="btn ghost" style="left:780px;top:139px;width:200px">Voreinstellung landen</div>
  </section>

  <section class="card" style="top:628px;height:712px">
    <h2 class="card-title">Kontaktdaten</h2>
    <p class="intro">In diesem Bereich können <b style="font-weight:500">Kontaktdaten</b> des objektes verwalten. Durch das Anklicken des jeweiligen Reilers können sie die Kontakt-Box&nbsp; vom Address-modus in den Handle-Modus (und umgekehrt) Umstellen.</p>

    <div class="contact" style="top:137px">
      <div class="contact-head">Domaininhaber
        <div class="mode"><b>Modus:</b><span class="check on"><svg width="10" height="8" viewBox="0 0 10 8"><path d="M1 4l3 3 5-6" stroke="#fff" stroke-width="1.8" fill="none"/></svg></span><span class="gap">Handle</span><span class="check"></span>Adresse</div>
      </div>
      <div class="contact-row"><span class="name">Domaininhaber</span><div class="field"></div>
        <div class="icon-btn" style="left:532px"><svg width="16" height="16" viewBox="0 0 16 16" fill="none" stroke="#333" stroke-width="1.6"><circle cx="6.5" cy="6.5" r="5"/><path d="M10 10l5 5"/></svg></div>
        <div class="icon-btn" style="left:571px"><svg width="18" height="14" viewBox="0 0 18 14" fill="none" stroke="#333" stroke-width="1.4"><circle cx="11" cy="4" r="3"/><path d="M5 13c0-3 3-5 6-5s6 2 6 5z"/><path d="M1 6h5M3.5 3.5v5"/></svg></div>
      </div>
    </div>

    <div class="contact" style="top:264px">
      <div class="contact-head">Administrativer Ansprechpartner
        <div class="mode"><b>Modus:</b><span class="check on"><svg width="10" height="8" viewBox="0 0 10 8"><path d="M1 4l3 3 5-6" stroke="#fff" stroke-width="1.8" fill="none"/></svg></span><span class="gap">Handle</span><span class="check"></span>Adresse</div>
      </div>
      <div class="contact-row"><span class="name">Administrativer Ansprechpartner*</span><div class="field"></div>
        <div class="icon-btn" style="left:532px"><svg width="16" height="16" viewBox="0 0 16 16" fill="none" stroke="#333" stroke-width="1.6"><circle cx="6.5" cy="6.5" r="5"/><path d="M10 10l5 5"/></svg></div>
        <div class="icon-btn" style="left:571px"><svg width="18" height="14" viewBox="0 0 18 14" fill="none" stroke="#333" stroke-width="1.4"><circle cx="11" cy="4" r="3"/><path d="M5 13c0-3 3-5 6-5s6 2 6 5z"/><path d="M1 6h5M3.5 3.5v5"/></svg></div>
      </div>
    </div>

    <div class="contact" style="top:391px">
      <div class="contact-head">Technischer Ansprechpartner
        <div class="mode"><b>Modus:</b><span class="check on"><svg width="10" height="8" viewBox="0 0 10 8"><path d="M1 4l3 3 5-6" stroke="#fff" stroke-width="1.8" fill="none"/></svg></span><span class="gap">Handle</span><span class="check"></span>Adresse</div>
      </div>
      <div class="contact-row"><span class="name">Technischer Ansprechpartner*</span><div class="field"></div>
        <div class="icon-btn" style="left:532px"><svg width="16" height="16" viewBox="0 0 16 16" fill="none" stroke="#333" stroke-width="1.6"><circle cx="6.5" cy="6.5" r="5"/><path d="M10 10l5 5"/></svg></div>
        <div class="icon-btn" style="left:571px"><svg width="18" height="14" viewBox="0 0 18 14" fill="none" stroke="#333" stroke-width="1.4"><circle cx="11" cy="4" r="3"/><path d="M5 13c0-3 3-5 6-5s6 2 6 5z"/><path d="M1 6h5M3.5 3.5v5"/></svg></div>
      </div>
    </div>

    <div class="contact" style="top:518px">
      <div class="contact-head">Buchhalterischer Ansprechpartner
        <div class="mode"><b>Modus:</b><span class="check on"><svg width="10" height="8" viewBox="0 0 10 8"><path d="M1 4l3 3 5-6" stroke="#fff" stroke-width="1.8" fill="none"/></svg></span><span class="gap">Handle</span><span class="check"></span>Adresse</div>
      </div>
      <div class="contact-row"><span class="name">Buchhalterischer Ansprechpartner*</span><div class="field"></div>
        <div class="icon-btn" style="left:532px"><svg width="16" height="16" viewBox="0 0 16 16" fill="none" stroke="#333" stroke-width="1.6"><circle cx="6.5" cy="6.5" r="5"/><path d="M10 10l5 5"/></svg></div>
        <div class="icon-btn" style="left:571px"><svg width="18" height="14" viewBox="0 0 18 14" fill="none" stroke="#333" stroke-width="1.4"><circle cx="11" cy="4" r="3"/><path d="M5 13c0-3 3-5 6-5s6 2 6 5z"/><path d="M1 6h5M3.5 3.5v5"/></svg></div>
      </div>
    </div>

    <div class="btn" style="left:794px;top:645px;width:186px">Kontaktdaten laden</div>
  </section>

  <section class="card" style="top:1361px;height:392px">
    <h2 class="card-title">Listen-Filter</h2>
    <span class="label" style="left:637px;top:45px">Zeilen pro siete</span>
    <div class="field select" style="left:740px;top:33px;width:86px;height:24px;font-size:12px">-
      <svg width="11" height="7" viewBox="0 0 11 7"><path d="M1 1l4.5 4.5L10 1" stroke="#444" stroke-width="1.5" fill="none"/></svg></div>
    <div class="more">Wreiter optionen <span class="plus">+</span></div>

    <span class="label" style="left:32px;top:106px">1. Nameserver</span><div class="field" style="left:180px;top:90px;width:240px;height:31px"></div>
    <span class="label" style="left:32px;top:153px">2. Nameserver</span><div class="field" style="left:180px;top:137px;width:240px;height:31px"></div>
    <span class="label" style="left:32px;top:200px">3. Nameserver</span><div class="field" style="left:180px;top:184px;width:240px;height:31px"></div>
    <span class="label" style="left:32px;top:247px">4. Nameserver</span><div class="field" style="left:180px;top:231px;width:240px;height:31px"></div>
    <span class="label" style="left:32px;top:294px">5. Nameserver</span><div class="field" style="left:180px;top:278px;width:240px;height:31px"></div>

    <span class="label" style="left:592px;top:106px">1. Hostip</span><div class="field" style="left:740px;top:90px;width:240px;height:31px"></div>
    <span class="label" style="left:592px;top:153px">2. Hostip</span><div class="field" style="left:740px;top:137px;width:240px;height:31px"></div>
    <span class="label" style="left:592px;top:200px">3. Hostip</span><div class="field" style="left:740px;top:184px;width:240px;height:31px"></div>
    <span class="label" style="left:592px;top:247px">4. Hostip</span><div class="field" style="left:740px;top:231px;width:240px;height:31px"></div>
    <span class="label" style="left:592px;top:294px">5. Hostip</span><div class="field" style="left:740px;top:278px;width:240px;height:31px"></div>

    <div class="btn" style="left:847px;top:325px;width:133px">Zonecheck</div>
  </section>

  <div class="footer-btn">Domainregisteren</div>
</div>
</body>
</html>
```